Home builders association trying to recruit young adults to consider careers in the skilled trades

We need a flyer that we can distribute in every high school to inform students and parents that careers in the skilled trades are very lucrative and have great opportunities for advancement and to own your own business. (similar to what the military and colleges do) Some examples of skilled trades include:

Carpenters are needed in all areas of construction and are often employed through the entire construction process. Thus, it is one of the most secure jobs within the industry. In the carpentry trade you will learn to: Frame floors, walls, ceilings and roof, Build concrete forms, Apply plywood, roof paper and shingles, build and set cabinets and countertops, Install doors, windows, trim and siding Install floor joists, rafters and trusses and more. $45,170 average national wage

HVACR: Install or repair heating, ventilation, and central air conditioning or refrigeration systems, including oil burners, hot-air furnaces and heating stoves. In the HVACR trade you will learn: How to maintain, repair and diagnose equipment related to HVACR technology, Energy auditing Green alternatives, Air conditioning design and layout, Refrigerant systems, System charging and system evacuation, Water treatment. $47,080 average national wage

Electrical: Modern life would not be possible without electricians. If you like to know how electric currents make things work, then this is the trade for you. Qualified electricians are always in demand. In the electrical trade you will learn to: Cut, bend and install metal conduits and wiring, Hook up electrical appliances, Install electrical switches and lighting fixtures, Wire door bells and fire alarms, Use equipment for testing circuitry. $54,110 average national wage

Plumbing: Nearly all areas of construction rely on plumbers. If you enjoy working with your hands and solving problems, then this is the trade for you. Plumbers install, repair, and maintain pipes in residential, commercial and/or industrial buildings. In the plumbing trade you will learn to: Identify hand and power tools Cut and install pipes and fittings, Install fixtures and hot water heaters Test water lines for leaks, Install sprinkler systems. $52,590 average national wage

Target Market(s)

Career Seekers

Font styles to use
Sans Serif

Requirements
Must have
• Our logo's and contact information:
Harbor Ridge Builders Association
www.harborridgeba.com/skilled-trades
www.groupsite.example/HRBASkilledTrades
555-214-7093
Nice to have
• I uploaded a skilled trades flyer that we used in the past but would love it to be more enticing to young people and more professional

```html
<!DOCTYPE html>
<html lang="en">
<head>
<meta charset="utf-8">
<title>Skilled Trades Flyer – Harbor Ridge Builders Association</title>
<link href="https://fonts.googleapis.com/css2?family=Oswald:wght@500;600;700&family=Roboto:wght@400;700&display=swap" rel="stylesheet">
<style>
  :root {
    --backdrop: #58595b;
    --navy: #1f2a78;
    --navy-deep: #17205e;
    --orange: #f5a81c;
    --yellow: #f7b500;
    --ink: #111111;
    --white: #ffffff;
    --photo-a: #6d6a66;
    --photo-b: #a59c8e;
  }
  * { margin: 0; padding: 0; box-sizing: border-box; }
  html, body { width: 1200px; height: 1200px; overflow: hidden; }
  body { background: var(--backdrop); font-family: "Roboto", Arial, sans-serif; position: relative; }

  .flyer-page {
    position: absolute; top: 250px; width: 442px; height: 572px;
    background: var(--white); transform: scale(1.2); transform-origin: 0 0;
    overflow: hidden; box-shadow: 0 2px 6px rgba(0,0,0,.35);
  }
  .flyer-page--front { left: 60px; }
  .flyer-page--back { left: 614px; }
  .page-shapes { position: absolute; inset: 0; width: 442px; height: 572px; }
  .abs { position: absolute; }

  /* front */
  .title-banner {
    left: 214px; top: 50px; width: 236px; height: 44px; background: var(--orange);
    transform: rotate(-15deg); transform-origin: center;
    display: flex; align-items: center; justify-content: center; white-space: nowrap;
    font-family: "Oswald", sans-serif; font-weight: 700; font-size: 30px; color: var(--ink);
    letter-spacing: .3px;
  }
  .intro-copy { left: 8px; top: 156px; width: 165px; font-size: 9.6px; line-height: 1.2; color: var(--navy-deep); }
  .intro-copy strong { display: block; margin-top: 10px; font-weight: 700; text-decoration: underline; }
  .question { right: 8px; top: 186px; text-align: right; font-family: "Oswald", sans-serif; font-weight: 600; font-size: 27px; line-height: 1.15; color: var(--white); }
  .question .accent { color: var(--yellow); }
  .question-rule { left: 268px; top: 257px; width: 174px; height: 2px; background: var(--yellow); }
  .job-list { left: 255px; top: 266px; list-style: none; font-family: "Oswald", sans-serif; font-weight: 600; font-size: 12px; color: var(--white); }
  .job-list li { height: 17.4px; display: flex; align-items: center; gap: 5px; letter-spacing: .2px; white-space: nowrap; }
  .tick { width: 10px; height: 10px; flex: none; }

  .photo-strip { left: 6px; top: 338px; width: 228px; height: 120px; background: var(--white); display: flex; gap: 4px; padding: 4px; }
  .photo-strip .photo { flex: 1; background: linear-gradient(160deg, var(--photo-b), var(--photo-a)); }

  .contact-tab { font-family: "Oswald", sans-serif; font-weight: 600; font-size: 14px; line-height: 18px; color: var(--ink); }
  .contact-lines { font-size: 7.8px; line-height: 11px; color: var(--white); white-space: nowrap; }
  .contact-lines .org { color: var(--yellow); font-weight: 700; }
  .contact-lines .row { display: flex; align-items: center; gap: 4px; }
  .contact-icon { width: 7px; height: 7px; flex: none; }

  .association-mark { display: flex; align-items: center; gap: 5px; font-family: "Oswald", sans-serif; font-weight: 600; font-size: 9.5px; line-height: 1.1; color: var(--navy); width: 110px; }
  .association-mark .square { width: 12px; height: 12px; background: var(--navy); flex: none; }

  /* back */
  .examples-heading { left: 52px; top: 14px; font-size: 10px; line-height: 1.25; color: var(--navy); }
  .examples-heading b { font-weight: 700; }
  .trade-tab { left: 0; width: 96px; height: 12px; padding-left: 6px; font-family: "Oswald", sans-serif; font-weight: 600; font-size: 9px; line-height: 12px; color: var(--ink); background: var(--orange); clip-path: polygon(0 0, 88% 0, 100% 100%, 0 100%); }
  .trade-copy { left: 8px; font-size: 7.1px; line-height: 1.22; color: var(--white); }
  .trade-icon { left: 10px; width: 26px; height: 28px; }
</style>
</head>
<body>

<section class="flyer-page flyer-page--front" aria-label="Flyer front">
  <svg class="page-shapes" viewBox="0 0 442 572" aria-hidden="true">
    <polygon points="0,137 160,122 230,197 0,297" fill="var(--orange)"/>
    <polygon points="230,197 442,122 442,494 0,494 0,312" fill="var(--navy)"/>
    <polygon points="200,572 442,480 442,572" fill="var(--white)"/>
    <polygon points="0,512 262,512 222,568 0,568" fill="var(--ink)"/>
    <polygon points="0,494 170,494 160,512 0,512" fill="var(--orange)"/>
    <rect x="0" y="568" width="442" height="4" fill="var(--orange)"/>
  </svg>

  <svg class="abs" style="left:0;top:0" width="442" height="200" viewBox="0 0 442 200">
    <defs>
      <linearGradient id="photoTone" x1="0" y1="0" x2="1" y2="1">
        <stop offset="0" stop-color="#3f4650"/><stop offset="1" stop-color="#9a8f80"/>
      </linearGradient>
      <linearGradient id="wordTone" x1="0" y1="0" x2="1" y2="1">
        <stop offset="0" stop-color="#f2f2f2"/><stop offset="1" stop-color="#d8d8d8"/>
      </linearGradient>
    </defs>
    <polygon role="img" aria-label="Photo of an electrician working on network cabling" points="0,0 205,0 160,122 0,137" fill="url(#photoTone)"/>
    <polygon role="img" aria-label="Word collage of trade names such as plumber, welder, roofer and floor layer" points="205,0 442,0 442,122 230,197 160,122" fill="url(#wordTone)"/>
  </svg>

  <div class="abs title-banner">SKILLED TRADES</div>

  <p class="abs intro-copy">Perhaps now more than ever, trades craftsmen are in high demand.
    <strong>SKILLED TRADES CAN PROVIDE A PROMISING CAREER PATH</strong>
    depending on a job seeker's skills &amp; location.</p>

  <h2 class="abs question">WHAT JOBS<br><span class="accent">INTEREST</span> YOU?</h2>
  <div class="abs question-rule"></div>

  <ul class="abs job-list">
    <li><svg class="tick" viewBox="0 0 10 10"><rect width="10" height="10" fill="var(--yellow)"/><path d="M2 5 L4.3 7.5 L8.5 2.5" stroke="var(--navy)" stroke-width="1.6" fill="none"/></svg>ELECTRICIAN</li>
    <li><svg class="tick" viewBox="0 0 10 10"><rect width="10" height="10" fill="var(--yellow)"/><path d="M2 5 L4.3 7.5 L8.5 2.5" stroke="var(--navy)" stroke-width="1.6" fill="none"/></svg>CARPENTER</li>
    <li><svg class="tick" viewBox="0 0 10 10"><rect width="10" height="10" fill="var(--yellow)"/><path d="M2 5 L4.3 7.5 L8.5 2.5" stroke="var(--navy)" stroke-width="1.6" fill="none"/></svg>HOME BUILDER</li>
    <li><svg class="tick" viewBox="0 0 10 10"><rect width="10" height="10" fill="var(--yellow)"/><path d="M2 5 L4.3 7.5 L8.5 2.5" stroke="var(--navy)" stroke-width="1.6" fill="none"/></svg>COMMERCIAL BUILDER</li>
    <li><svg class="tick" viewBox="0 0 10 10"><rect width="10" height="10" fill="var(--yellow)"/><path d="M2 5 L4.3 7.5 L8.5 2.5" stroke="var(--navy)" stroke-width="1.6" fill="none"/></svg>REMODELERS</li>
    <li><svg class="tick" viewBox="0 0 10 10"><rect width="10" height="10" fill="var(--yellow)"/><path d="M2 5 L4.3 7.5 L8.5 2.5" stroke="var(--navy)" stroke-width="1.6" fill="none"/></svg>PAINTING CONTRACTOR</li>
    <li><svg class="tick" viewBox="0 0 10 10"><rect width="10" height="10" fill="var(--yellow)"/><path d="M2 5 L4.3 7.5 L8.5 2.5" stroke="var(--navy)" stroke-width="1.6" fill="none"/></svg>DRYWALL CONTRACTOR</li>
    <li><svg class="tick" viewBox="0 0 10 10"><rect width="10" height="10" fill="var(--yellow)"/><path d="M2 5 L4.3 7.5 L8.5 2.5" stroke="var(--navy)" stroke-width="1.6" fill="none"/></svg>MASON</li>
    <li><svg class="tick" viewBox="0 0 10 10"><rect width="10" height="10" fill="var(--yellow)"/><path d="M2 5 L4.3 7.5 L8.5 2.5" stroke="var(--navy)" stroke-width="1.6" fill="none"/></svg>HVAC TECHNICIAN</li>
    <li><svg class="tick" viewBox="0 0 10 10"><rect width="10" height="10" fill="var(--yellow)"/><path d="M2 5 L4.3 7.5 L8.5 2.5" stroke="var(--navy)" stroke-width="1.6" fill="none"/></svg>PLUMBER</li>
    <li><svg class="tick" viewBox="0 0 10 10"><rect width="10" height="10" fill="var(--yellow)"/><path d="M2 5 L4.3 7.5 L8.5 2.5" stroke="var(--navy)" stroke-width="1.6" fill="none"/></svg>ALUMINUM INSTALLERS</li>
    <li><svg class="tick" viewBox="0 0 10 10"><rect width="10" height="10" fill="var(--yellow)"/><path d="M2 5 L4.3 7.5 L8.5 2.5" stroke="var(--navy)" stroke-width="1.6" fill="none"/></svg>TILE SETTERS</li>
  </ul>

  <div class="abs photo-strip">
    <div class="photo" role="img" aria-label="Photo of a young tradesman holding a tool"></div>
    <div class="photo" role="img" aria-label="Photo of a worker in a hard hat using a power tool"></div>
    <div class="photo" role="img" aria-label="Photo of an electrician wiring a panel"></div>
  </div>

  <div class="abs contact-tab" style="left:20px;top:494px">CONTACT US</div>
  <div class="abs contact-lines" style="left:8px;top:516px">
    <div class="row"><span class="contact-icon"></span><span class="org">Harbor Ridge Builders Association</span></div>
    <div class="row"><svg class="contact-icon" viewBox="0 0 8 8"><circle cx="4" cy="4" r="3.3" fill="none" stroke="var(--yellow)" stroke-width="1"/></svg>www.harborridgeba.com/skilled-trades</div>
    <div class="row"><svg class="contact-icon" viewBox="0 0 8 8"><circle cx="4" cy="4" r="3.5" fill="var(--yellow)"/></svg>www.groupsite.example/HRBASkilledTrades</div>
    <div class="row"><svg class="contact-icon" viewBox="0 0 8 8"><path d="M1.5 1 L3 1 L3.6 2.8 L2.7 3.5 Q3.5 5 4.6 5.4 L5.3 4.5 L7 5.1 L7 6.6 Q3.5 7.2 1 2.5 Z" fill="var(--yellow)"/></svg>555-214-7093</div>
  </div>

  <div class="abs association-mark" style="left:326px;top:514px"><span class="square"></span><span>Harbor Ridge Builders Association</span></div>
</section>

<section class="flyer-page flyer-page--back" aria-label="Flyer back">
  <svg class="page-shapes" viewBox="0 0 442 572">
    <defs>
      <linearGradient id="photoToneBack" x1="0" y1="0" x2="1" y2="1">
        <stop offset="0" stop-color="#b9a98f"/><stop offset="1" stop-color="#5f6f7d"/>
      </linearGradient>
    </defs>
    <polygon points="0,92 254,57 305,132 441,100 441,494 0,455" fill="var(--navy)"/>
    <polygon role="img" aria-label="Photo of a carpenter in a cap hammering siding" points="215,0 441,0 441,100 305,132" fill="url(#photoToneBack)"/>
    <polygon points="305,132 441,100 441,190" fill="var(--orange)"/>
    <polygon points="292,512 441,512 441,568 252,568" fill="var(--ink)"/>
    <polygon points="290,494 441,494 441,512 282,512" fill="var(--orange)"/>
    <rect x="0" y="568" width="442" height="4" fill="var(--orange)"/>
  </svg>

  <p class="abs examples-heading">Some example of<br><b>SKILL TRADES include:</b></p>

  <svg class="abs trade-icon" style="top:57px" viewBox="0 0 26 28" aria-hidden="true">
    <g stroke="var(--orange)" stroke-width="2.4" fill="none" stroke-linecap="round">
      <path d="M6 4 L6 26"/><path d="M2 5 L11 5"/><path d="M17 6 L17 26"/><path d="M14 4 L21 4 L21 9 L14 9 Z"/><path d="M23 12 L23 26"/>
    </g>
  </svg>
  <div class="abs trade-tab" style="top:95px">CARPENTERS</div>
  <p class="abs trade-copy" style="top:110px;width:290px">Carpenters are needed in all areas of construction and are often employed through the entire construction process. Thus, it is one of the most secure jobs within the industry. In the carpentry trade you will learn to: Frame floors, walls, ceilings and roof, Build concrete forms, Apply plywood, roof paper and shingles, build and set cabinets and countertops, Install doors, windows, trim and siding Install floor joists, rafters and trusses and more. $45,170 average national wage</p>

  <svg class="abs trade-icon" style="top:182px;width:30px" viewBox="0 0 30 28" aria-hidden="true">
    <g stroke="var(--orange)" stroke-width="2" fill="none" stroke-linecap="round">
      <rect x="2" y="3" width="26" height="12" rx="2"/><path d="M6 11 L24 11"/><path d="M9 19 Q7 22 9 25"/><path d="M15 19 Q13 22 15 25"/><path d="M21 19 Q19 22 21 25"/>
    </g>
  </svg>
  <div class="abs trade-tab" style="top:217px">HVACR</div>
  <p class="abs trade-copy" style="top:232px;width:426px">Install or repair heating, ventilation, and central air conditioning or refrigeration systems, including oil burners, hot-air furnaces and heating stoves. In the HVACR trade you will learn: How to maintain, repair and diagnose equipment related to HVACR technology, Energy auditing Green alternatives, Air conditioning design and layout, Refrigerant systems, System charging and system evacuation, Water treatment. $47,080 average national wage</p>

  <svg class="abs trade-icon" style="top:276px;width:32px" viewBox="0 0 32 28" aria-hidden="true">
    <g stroke="var(--orange)" stroke-width="2.2" fill="none" stroke-linecap="round">
      <path d="M2 14 L8 14"/><path d="M8 8 L14 8 L14 20 L8 20 Z"/><path d="M14 11 L18 11"/><path d="M14 17 L18 17"/><path d="M22 14 L30 14"/><path d="M22 9 L22 19"/>
    </g>
  </svg>
  <div class="abs trade-tab" style="top:307px">ELECTRICAL</div>
  <p class="abs trade-copy" style="top:323px;width:426px">Modern life would not be possible without electricians. If you like to know how electric currents make things work, then this is the trade for you. Qualified electricians are always in demand. In the electrical trade you will learn to: Cut, bend and install metal conduits and wiring, Hook up electrical appliances, Install electrical switches and lighting fixtures, Wire door bells and fire alarms, Use equipment for testing circuitry. $54,110 average national wage</p>

  <svg class="abs trade-icon" style="top:363px" viewBox="0 0 26 28" aria-hidden="true">
    <g stroke="var(--orange)" stroke-width="3" fill="none" stroke-linecap="round">
      <path d="M4 3 L4 14 Q4 20 10 20 L22 20"/><path d="M22 14 L22 26"/><path d="M14 22 L14 26"/>
    </g>
  </svg>
  <div class="abs trade-tab" style="top:397px">PLUMBING</div>
  <p class="abs trade-copy" style="top:412px;width:426px">Nearly all areas of construction rely on plumbers. If you enjoy working with your hands and solving problems, then this is the trade for you. Plumbers install, repair, and maintain pipes in residential, commercial and/or industrial buildings. In the plumbing trade you will learn to: Identify hand and power tools Cut and install pipes and fittings, Install fixtures and hot water heaters Test water lines for leaks, Install sprinkler systems. $52,590 average national wage</p>

  <div class="abs association-mark" style="left:12px;top:514px"><span class="square"></span><span>Harbor Ridge Builders Association</span></div>

  <div class="abs contact-tab" style="left:330px;top:494px">CONTACT US</div>
  <div class="abs contact-lines" style="right:8px;top:516px;text-align:right">
    <div class="row" style="justify-content:flex-end"><span class="org">Harbor Ridge Builders Association</span><span class="contact-icon"></span></div>
    <div class="row" style="justify-content:flex-end">www.harborridgeba.com/skilled-trades<svg class="contact-icon" viewBox="0 0 8 8"><circle cx="4" cy="4" r="3.3" fill="none" stroke="var(--yellow)" stroke-width="1"/></svg></div>
    <div class="row" style="justify-content:flex-end">www.groupsite.example/HRBASkilledTrades<svg class="contact-icon" viewBox="0 0 8 8"><circle cx="4" cy="4" r="3.5" fill="var(--yellow)"/></svg></div>
    <div class="row" style="justify-content:flex-end">555-214-7093<svg class="contact-icon" viewBox="0 0 8 8"><path d="M1.5 1 L3 1 L3.6 2.8 L2.7 3.5 Q3.5 5 4.6 5.4 L5.3 4.5 L7 5.1 L7 6.6 Q3.5 7.2 1 2.5 Z" fill="var(--yellow)"/></svg></div>
  </div>
</section>

</body>
</html>
```